High end boutique food product label

We are looking for a label design to be used on our range of high end food products. We don't have a design or colour scheme in mind and are interested to see what ideas are submitted.
We would like it to feel sophisticated, chic, and eye-catching.
All of our products are handmade in Australia using Australian ingredients.
The graphics for the label will need to be scaleable to be fit a variety of labels from small squat jars with labels sized 3.5cm high and 7cm wide, to tall thin bottles with labels that are 14cm high and 4.5cm wide.
We would be interested in working with the winning designer to create these different sized labels.
The label submitted for this project should be 14cm high and 4.5cm wide, it should include our logo (file supplied in .jpeg and .ai), the product name 'Extra Virgin Olive Oil' and the size '250ml'.
This is just the front label on a bottle, we are not expecting a rear label to be created currently.
You are welcome to use any fonts you think will look good but the fonts used in our logo are Allaina Medium and Bebas Kai Regular.

```html
<!DOCTYPE html>
<html lang="en">
<head>
<meta charset="utf-8">
<title>Extra Virgin Olive Oil – Front Label</title>
<link rel="stylesheet" href="https://fonts.googleapis.com/css2?family=Young+Serif&family=Montserrat:wght@500&display=swap">
<style>
  :root {
    --page: #ffffff;
    --label-black: #1b1a1a;
    --cream: #f4f1ec;
    --copper: #c18a52;
    --copper-light: #e7b27a;
    --copper-dark: #7a4a22;
  }
  * { box-sizing: border-box; margin: 0; padding: 0; }
  html, body {
    width: 1200px;
    height: 1200px;
    overflow: hidden;
    background: var(--page);
  }
  .canvas {
    position: relative;
    width: 1200px;
    height: 1200px;
  }
  .label {
    position: absolute;
    left: 424px;
    top: 60px;
    width: 351px;
    height: 1080px;
    background: var(--label-black);
    overflow: hidden;
  }
  .branch-artwork {
    position: absolute;
    left: 0;
    top: 0;
    width: 351px;
    height: 460px;
  }
  .brand-name {
    position: absolute;
    left: 86px;
    top: 352px;
    width: 250px;
    text-align: center;
    color: var(--cream);
    font-family: "Young Serif", serif;
    font-size: 32px;
    line-height: 1;
    white-space: nowrap;
  }
  .product-name {
    position: absolute;
    left: 0;
    top: 580px;
    width: 351px;
    text-align: center;
    color: var(--cream);
    font-family: "Young Serif", serif;
    font-weight: 400;
    line-height: 1;
  }
  .product-name-sub {
    display: block;
    font-size: 33px;
  }
  .product-name-main {
    display: block;
    font-size: 70px;
    margin-top: 6px;
    letter-spacing: -0.5px;
  }
  .origin-badge {
    position: absolute;
    left: 105px;
    top: 776px;
    width: 140px;
    height: 140px;
  }
  .volume {
    position: absolute;
    left: 0;
    top: 992px;
    width: 351px;
    text-align: center;
    color: var(--cream);
    font-family: "Montserrat", sans-serif;
    font-weight: 500;
    font-size: 17px;
    letter-spacing: 0.5px;
  }
  .copper-band {
    position: absolute;
    left: 0;
    top: 1043px;
    width: 351px;
    height: 26px;
    background: linear-gradient(90deg, var(--copper-dark) 0%, var(--copper-light) 30%, var(--copper) 55%, var(--copper-light) 80%, var(--copper-dark) 100%);
  }
</style>
</head>
<body>
<main class="canvas">
  <section class="label">
    <svg class="branch-artwork" viewBox="0 0 351 460" role="img" aria-label="Copper olive branch with leaves and olives sweeping across the top-left corner">
      <defs>
        <linearGradient id="branch-tone" x1="0" y1="0" x2="1" y2="1">
          <stop offset="0" stop-color="#d9a36c"/>
          <stop offset="0.5" stop-color="#a8682f"/>
          <stop offset="1" stop-color="#6b3f1c"/>
        </linearGradient>
      </defs>
      <path d="M0 0 H351 V40 C300 110 220 180 150 230 C100 270 70 330 40 460 H0 Z" fill="url(#branch-tone)" opacity="0.85"/>
    </svg>

    <p class="brand-name">Hartley Pantry</p>

    <h1 class="product-name">
      <span class="product-name-sub">Extra Virgin</span>
      <span class="product-name-main">Olive Oil</span>
    </h1>

    <svg class="origin-badge" viewBox="0 0 140 140" role="img" aria-label="Origin badge">
      <circle cx="70" cy="70" r="62" fill="none" stroke="#f4f1ec" stroke-width="2"/>
    </svg>

    <p class="volume">250ml / 8,45oz</p>

    <div class="copper-band"></div>
  </section>
</main>
</body>
</html>
```